Business Card Design Project

Please create a custom business card for Silverpine Golf Academy. The logo is attached to this brief.

Colours could be based on Blue, black, red, or white color. Colors like orange, green, purple, pink are not preferable.

Here is the link to the logo project : http://jobs.brieflantern.com/job.aspx?id=413057

Questions can be posted on the Discussion Board.

```html
<!DOCTYPE html>
<html lang="en">
<head>
<meta charset="utf-8">
<title>Silverpine Golf Academy – Business Card</title>
<link rel="stylesheet" href="https://fonts.googleapis.com/css2?family=Open+Sans:wght@400;600;700&display=swap">
<style>
  :root {
    --backdrop: #dcd9d3;
    --card-blue-light: #0e3a86;
    --card-blue-dark: #072a68;
    --ink-white: #ffffff;
    --ink-soft: #d4ddef;
    --shadow: rgba(20, 24, 40, 0.28);
  }
  * { margin: 0; padding: 0; box-sizing: border-box; }
  html, body {
    width: 1200px; height: 871px; overflow: hidden;
    background: var(--backdrop);
    font-family: "Open Sans", Arial, sans-serif;
  }
  .canvas {
    width: 1200px; height: 871px;
    display: flex; align-items: center; justify-content: center; gap: 40px;
  }
  .card {
    position: relative;
    width: 560px; height: 320px;
    background: radial-gradient(ellipse at 40% 35%, var(--card-blue-light) 0%, var(--card-blue-dark) 100%);
    box-shadow: 0 14px 30px var(--shadow);
    color: var(--ink-white);
  }
  .brand {
    display: flex; flex-direction: column; align-items: center;
    text-align: center;
  }
  .brand-dot {
    width: 54px; height: 54px; border-radius: 50%;
    background: var(--ink-white);
    margin-bottom: 10px;
  }
  .brand-name {
    font-weight: 600; font-size: 24px; line-height: 1.15;
    color: var(--ink-white);
    letter-spacing: 0.2px;
  }
  .card-front .brand {
    position: absolute; left: 0; right: 0; top: 96px;
  }
  .card-back .brand {
    position: absolute; left: 40px; top: 96px; width: 230px;
  }
  .contact {
    position: absolute; left: 310px; top: 78px; width: 230px;
  }
  .contact-name {
    font-weight: 700; font-size: 18px; letter-spacing: 0.6px;
  }
  .contact-role {
    font-size: 13px; color: var(--ink-soft); margin-bottom: 16px;
  }
  .contact-address {
    font-size: 13px; line-height: 1.5; color: var(--ink-soft); margin-bottom: 12px;
  }
  .contact-line {
    display: flex; align-items: center; gap: 12px;
    font-size: 13px; color: var(--ink-soft); line-height: 24px;
  }
  .contact-line svg { width: 14px; height: 14px; flex: none; }
</style>
</head>
<body>
<main class="canvas">
  <section class="card card-front" aria-label="Card front">
    <div class="brand">
      <span class="brand-dot"></span>
      <span class="brand-name">Silverpine Golf Academy</span>
    </div>
  </section>

  <section class="card card-back" aria-label="Card back">
    <div class="brand">
      <span class="brand-dot"></span>
      <span class="brand-name">Silverpine Golf<br>Academy</span>
    </div>
    <div class="contact">
      <p class="contact-name">Daniel Harwick</p>
      <p class="contact-role">President</p>
      <p class="contact-address">PO Box 218<br>Westbrook Falls, RI 02931</p>
      <p class="contact-line">
        <svg viewBox="0 0 16 16" aria-hidden="true"><path fill="#d4ddef" d="M3.5 1.5l2.4 0 1 3.2-1.6 1.2a9 9 0 0 0 4.8 4.8l1.2-1.6 3.2 1v2.4c0 .8-.7 1.5-1.5 1.5C6.8 14 2 9.2 2 3c0-.8.7-1.5 1.5-1.5z"/></svg>
        +49 (0) 151 20473518
      </p>
      <p class="contact-line">
        <svg viewBox="0 0 16 16" aria-hidden="true"><rect x="1.5" y="3.5" width="13" height="9" fill="none" stroke="#d4ddef" stroke-width="1.4"/><path d="M1.5 3.5l6.5 5 6.5-5" fill="none" stroke="#d4ddef" stroke-width="1.4"/></svg>
        dan@silverpinegolf.com
      </p>
      <p class="contact-line">
        <svg viewBox="0 0 16 16" aria-hidden="true"><circle cx="8" cy="8" r="6.3" fill="none" stroke="#d4ddef" stroke-width="1.3"/><ellipse cx="8" cy="8" rx="2.8" ry="6.3" fill="none" stroke="#d4ddef" stroke-width="1.1"/><path d="M1.7 8h12.6M2.6 5h10.8M2.6 11h10.8" stroke="#d4ddef" stroke-width="1"/></svg>
        www.silverpinegolf.com
      </p>
    </div>
  </section>
</main>
</body>
</html>
```